Harmony Swift Care Business card

We want a business card that matches our business theme. Our website is www.swiftcarehub.example
The company name is Harmony Swift Care
The persons having the business cards will be doctors
My logo is attached.
We have a drive-thru medical center where our motto is Fast, Reliable, and Convenient. Our goal is to change the medical space while utilizing technologies, keeping a professional and clean look

Medical

Info on the card should be: Name, Position, Cell number, website, email address, possibly the office line as well

Requirements
Must have
• Logo
Nice to have
• Professional medical feel with our logo colors incorporated

```html
<!DOCTYPE html>
<html lang="en">
<head>
<meta charset="utf-8">
<title>Harmony Swift Care – Business Card</title>
<link rel="stylesheet" href="https://fonts.googleapis.com/css2?family=Open+Sans:ital,wght@0,400;0,700;0,800;1,400&display=swap">
<style>
  :root {
    --navy: #1d3f9e;
    --navy-deep: #17358c;
    --royal: #2251b0;
    --sky: #3bb4ea;
    --ink: #3a3a3a;
    --paper: #ffffff;
    --backdrop: #26282c;
  }
  html, body {
    margin: 0;
    width: 1200px;
    height: 900px;
    overflow: hidden;
    background: var(--backdrop);
    font-family: "Open Sans", Arial, sans-serif;
  }
  .card {
    position: absolute;
    left: 250px;
    width: 700px;
    height: 400px;
    overflow: hidden;
    box-shadow: 0 16px 40px rgba(0,0,0,.5);
  }
  .card-front { top: 35px; background: var(--paper); }
  .card-back  { top: 465px; background: var(--navy); }

  .card-waves {
    position: absolute;
    inset: 0;
    width: 700px;
    height: 400px;
  }
  .brand {
    position: absolute;
    left: 60px;
    top: 112px;
    width: 290px;
  }
  .brand-row {
    display: flex;
    align-items: center;
    gap: 14px;
  }
  .brand-name {
    margin: 0;
    color: var(--navy);
    font-weight: 800;
    font-size: 28px;
    line-height: 1.05;
  }
  .brand-mark {
    flex: none;
    width: 62px;
    height: 62px;
    border-radius: 50%;
    background: var(--navy);
  }
  .brand-tagline {
    margin: 12px 0 0;
    color: var(--ink);
    font-size: 11px;
    letter-spacing: .4px;
    text-transform: uppercase;
  }
  .divider {
    position: absolute;
    left: 374px;
    top: 100px;
    width: 2px;
    height: 156px;
    background: var(--navy);
  }
  .person {
    position: absolute;
    left: 400px;
    top: 98px;
  }
  .person-name {
    margin: 0;
    color: var(--navy);
    font-weight: 800;
    font-size: 22px;
    line-height: 1.2;
    text-transform: uppercase;
    letter-spacing: .4px;
  }
  .person-role {
    margin: 0 0 12px;
    color: var(--ink);
    font-style: italic;
    font-size: 14px;
  }
  .contact-list {
    list-style: none;
    margin: 0;
    padding: 0;
  }
  .contact-item {
    display: flex;
    align-items: center;
    gap: 9px;
    color: var(--ink);
    font-size: 13.5px;
    line-height: 23px;
  }
  .contact-icon {
    width: 13px;
    height: 13px;
    flex: none;
    fill: var(--sky);
  }

  .back-pattern {
    position: absolute;
    inset: 0;
    background: linear-gradient(135deg, var(--navy-deep) 0%, var(--royal) 55%, #2a63bf 100%);
  }
  .back-brand {
    position: absolute;
    right: 34px;
    bottom: 30px;
    display: flex;
    align-items: center;
    gap: 10px;
  }
  .back-mark {
    width: 40px;
    height: 40px;
    border-radius: 50%;
    background: var(--paper);
  }
  .back-name {
    margin: 0;
    color: var(--paper);
    font-weight: 800;
    font-size: 17px;
  }
</style>
</head>
<body>
  <section class="card card-front" aria-label="Business card front">
    <svg class="card-waves" viewBox="0 0 1050 600" preserveAspectRatio="none" aria-hidden="true">
      <path d="M0 385 C 260 370, 430 465, 640 545 C 760 585, 880 600, 1050 600 L 0 600 Z" fill="#3bb4ea"/>
      <path d="M0 397 C 250 387, 420 482, 620 560 C 720 595, 800 600, 850 600 L 0 600 Z" fill="#ffffff"/>
      <path d="M0 410 C 240 402, 400 497, 600 575 C 650 592, 690 600, 720 600 L 0 600 Z" fill="#1d3f9e"/>
    </svg>

    <div class="brand">
      <div class="brand-row">
        <h1 class="brand-name">Harmony<br>Swift Care</h1>
        <span class="brand-mark" aria-hidden="true"></span>
      </div>
      <p class="brand-tagline">Fast | Reliable | Convenient</p>
    </div>

    <div class="divider" aria-hidden="true"></div>

    <div class="person">
      <h2 class="person-name">Daniel Arbor</h2>
      <p class="person-role">President</p>
      <ul class="contact-list">
        <li class="contact-item">
          <svg class="contact-icon" viewBox="0 0 18 18" aria-hidden="true"><path d="M5 1h8a1 1 0 0 1 1 1v14a1 1 0 0 1-1 1H5a1 1 0 0 1-1-1V2a1 1 0 0 1 1-1zm1 2v10h6V3zm3 11a1 1 0 1 0 0 2 1 1 0 0 0 0-2z"/></svg>
          1300 555 014
        </li>
        <li class="contact-item">
          <svg class="contact-icon" viewBox="0 0 18 18" aria-hidden="true"><path d="M4 1l3 4-2 2c1 2.5 3.5 5 6 6l2-2 4 3-2 3C8 17 1 10 1 4z"/></svg>
          1300 555 014
        </li>
        <li class="contact-item">
          <svg class="contact-icon" viewBox="0 0 18 18" aria-hidden="true"><path d="M1 4h16v10H1zm1.5 1L9 10l6.5-5z"/></svg>
          daniel@swiftcarehub.example
        </li>
        <li class="contact-item">
          <svg class="contact-icon" viewBox="0 0 18 18" aria-hidden="true"><circle cx="9" cy="9" r="8"/><path d="M1 9h16M9 1c3 3 3 13 0 16M9 1c-3 3-3 13 0 16" stroke="#fff" stroke-width="1.2" fill="none"/></svg>
          www.swiftcarehub.example
        </li>
      </ul>
    </div>
  </section>

  <section class="card card-back" aria-label="Business card back">
    <div class="back-pattern" role="img" aria-label="Repeating pattern of brand marks in tones of blue"></div>
    <div class="back-brand">
      <span class="back-mark" aria-hidden="true"></span>
      <p class="back-name">Harmony Swift Care</p>
    </div>
  </section>
</body>
</html>
```